Re-style home page - eye-catching and unique design for social commerce website

We need a new concept design for TrindaMo's home page.
We don't want to make huge changes but creating a more professional and eye-catching style.

We need to look very serious like a professional services company and in the same time to look like a social network for e-commerce.

Our logo is very captive and you can use to creating something of harmonious.

This is a re-style and I'm excepted to see unique and fresh design like Clovaret.

Target Market(s)

e-commerce and social

Industry/Entity Type

Social

Number of Pages Required

1 page

Font styles to use
Serif
Sans Serif

Requirements
Must have
• An eye-catching result.
• Search bar with logo and Login How it works and business
• The slogan with login and signup.
• Footer links.
Nice to have
• I would like to open the home page and see only two clear ways:
• -Consumer
• --Search
• --The slogan
• --Login and Signup
• --How it works
• -Business
• --Go to Business area
• Background: City, Shopping.
Should not have
• Scrollbar style!

```html
<!DOCTYPE html>
<html lang="en">
<head>
<meta charset="utf-8">
<title>TrindaMo – Shop directly from your profile</title>
<link rel="stylesheet" href="https://fonts.googleapis.com/css2?family=Open+Sans:wght@400;600;700&family=Arimo:wght@400;700&display=swap">
<style>
  :root {
    --navy: #262460;
    --navy-button: #25235c;
    --red-panel: rgba(232, 62, 60, 0.92);
    --red-search-top: #f0604a;
    --red-search-bottom: #e23a3c;
    --white: #ffffff;
    --field: #f2f2f2;
    --field-text: #3a3a3a;
    --social-blue: #2b4590;
    --footer-bg: rgba(38, 38, 38, 0.78);
  }
  * { box-sizing: border-box; margin: 0; padding: 0; }
  html, body { width: 1200px; height: 785px; overflow: hidden; background: #ddd; }
  body { position: relative; font-family: "Arimo", Arial, sans-serif; }

  /* Header */
  .site-header {
    position: absolute; left: 0; top: 0; width: 1200px; height: 84px;
    background: var(--navy); z-index: 5;
  }
  .brand {
    position: absolute; left: 98px; top: 20px;
    font-family: "Open Sans", sans-serif; font-weight: 700; font-size: 34px;
    color: var(--white); letter-spacing: -0.5px; line-height: 44px;
  }
  .search {
    position: absolute; left: 331px; top: 25px; width: 470px; height: 39px;
    background: var(--white); border-radius: 3px;
  }
  .search-button {
    position: absolute; right: 3px; top: 3px; width: 103px; height: 33px;
    border-radius: 3px;
    background: linear-gradient(var(--red-search-top), var(--red-search-bottom));
    color: var(--white); font-family: "Open Sans", sans-serif; font-weight: 700;
    font-size: 14px; line-height: 33px; text-align: center; letter-spacing: 0.3px;
  }
  .main-nav { position: absolute; top: 37px; color: var(--white); font-size: 15px; }
  .main-nav span { position: absolute; white-space: nowrap; }

  /* Photo mosaic */
  .tile { position: absolute; }
  .col-1 { left: 0; width: 267px; }
  .col-2 { left: 267px; width: 270px; }
  .col-3 { left: 537px; width: 270px; }
  .col-4 { left: 807px; width: 270px; }
  .col-5 { left: 1077px; width: 123px; }

  /* Welcome panel */
  .welcome {
    position: absolute; left: 148px; top: 309px; width: 901px; height: 260px;
    background: var(--red-panel); border-radius: 4px; z-index: 4;
  }
  .welcome-title {
    position: absolute; left: 26px; top: 32px;
    font-family: "Open Sans", sans-serif; font-weight: 600; font-size: 30px;
    color: var(--white); letter-spacing: -0.5px;
    text-shadow: 0 1px 2px rgba(0,0,0,0.35);
  }
  .field {
    position: absolute; top: 105px; width: 195px; height: 41px;
    background: var(--field); border-radius: 3px;
    box-shadow: inset 0 1px 3px rgba(0,0,0,0.25);
    font-family: "Open Sans", sans-serif; font-weight: 600; font-size: 14px;
    color: var(--field-text); line-height: 41px; padding-left: 13px;
  }
  .field-username { left: 25px; }
  .field-password { left: 256px; padding-left: 24px; }
  .signup-button {
    position: absolute; left: 313px; top: 176px; width: 138px; height: 40px;
    background: var(--navy-button); border-radius: 2px;
    font-family: "Open Sans", sans-serif; font-weight: 600; font-size: 20px;
    color: var(--white); text-align: center; line-height: 38px;
  }
  .divider {
    position: absolute; left: 471px; top: 26px; width: 1px; height: 210px;
    background: rgba(255,255,255,0.35);
  }
  .social-login {
    position: absolute; left: 545px; top: 102px; width: 289px; height: 55px;
    background: var(--social-blue); border: 2px solid var(--white); border-radius: 4px;
    color: var(--white); font-size: 21px; line-height: 51px; text-align: center;
  }

  /* Footer links */
  .footer-links {
    position: absolute; left: 159px; top: 705px; width: 882px; height: 50px;
    background: var(--footer-bg); border-radius: 3px; z-index: 4;
    color: var(--white); font-size: 14px; line-height: 50px;
  }
  .footer-links span { position: absolute; white-space: nowrap; }
</style>
</head>
<body>

<header class="site-header">
  <div class="brand">TrindaMo</div>
  <div class="search">
    <div class="search-button">SEARCH</div>
  </div>
  <nav class="main-nav">
    <span style="left:838px">Login</span>
    <span style="left:916px">How it works</span>
    <span style="left:1038px">Business</span>
  </nav>
</header>

<main class="mosaic">
  <div class="tile col-1" style="top:84px;height:182px;background:linear-gradient(135deg,#e9dcb4,#fbf4cf 60%,#c9a878)" role="img" aria-label="Dream catcher with feathers in warm sunlight"></div>
  <div class="tile col-1" style="top:266px;height:245px;background:linear-gradient(90deg,#5f5550,#b7aaa0 55%,#e8e4e0)" role="img" aria-label="Portrait of a young woman with dark hair"></div>
  <div class="tile col-1" style="top:511px;height:274px;background:radial-gradient(circle at 40% 40%,#8aa1a4,#2e3b3f 70%,#161d20)" role="img" aria-label="Close-up of two crossed forks"></div>

  <div class="tile col-2" style="top:84px;height:486px;background:linear-gradient(160deg,#9aa6a1,#7f8c88 60%,#6e7774)" role="img" aria-label="Man in a suit walking across a street"></div>
  <div class="tile col-2" style="top:570px;height:45px;background:linear-gradient(#c8cdcd,#9ca4a5)" role="img" aria-label="Grey sea waves"></div>
  <div class="tile col-2" style="top:615px;height:170px;background:linear-gradient(135deg,#eaf2e5,#b57b45 45%,#2f5b74)" role="img" aria-label="Wooden beam structure against the sky"></div>

  <div class="tile col-3" style="top:84px;height:182px;background:linear-gradient(135deg,#d7a158,#dfe6ef 35%,#eef2f7)" role="img" aria-label="Skateboard leaning beside a stool"></div>
  <div class="tile col-3" style="top:266px;height:304px;background:linear-gradient(#b7c9d3,#dde3e6 50%,#9aa3a6)" role="img" aria-label="Blurred bright interior"></div>
  <div class="tile col-3" style="top:570px;height:215px;background:linear-gradient(#c4cbd1,#8d9399 55%,#8a6a4e)" role="img" aria-label="Stacked logs in a misty forest"></div>

  <div class="tile col-4" style="top:84px;height:286px;background:linear-gradient(135deg,#8c7b66,#d9d2c4 50%,#efe9df)" role="img" aria-label="Fashion model wrapped in paper strips"></div>
  <div class="tile col-4" style="top:370px;height:300px;background:linear-gradient(#6d6f70,#3e4143 60%,#242628)" role="img" aria-label="Record player in close-up"></div>
  <div class="tile col-4" style="top:670px;height:115px;background:linear-gradient(#3a6a95,#1f3c5c)" role="img" aria-label="Retro gadget on a blue table"></div>

  <div class="tile col-5" style="top:84px;height:182px;background:linear-gradient(#cfc3cb,#a9909f 60%,#5e3a52)" role="img" aria-label="Bare tree in purple fog"></div>
  <div class="tile col-5" style="top:266px;height:199px;background:linear-gradient(135deg,#eef0f3,#b8c2cc)" role="img" aria-label="Pale flowing hair"></div>
  <div class="tile col-5" style="top:465px;height:320px;background:linear-gradient(90deg,#f2f2f0,#d9dcd8 60%,#6a6f72)" role="img" aria-label="Woman with floral hair by a white door"></div>
</main>

<section class="welcome">
  <h1 class="welcome-title">Shop Directly from your profile</h1>
  <div class="field field-username">Username</div>
  <div class="field field-password">Password</div>
  <div class="signup-button">Sign Up</div>
  <div class="divider"></div>
  <div class="social-login">Login with Kinloop</div>
</section>

<footer class="footer-links">
  <span style="left:37px">ABOUT TRINDAMO</span>
  <span style="left:163px">|</span>
  <span style="left:190px">BLOG</span>
  <span style="left:244px">|</span>
  <span style="left:271px">BUSINESS</span>
  <span style="left:355px">|</span>
  <span style="left:382px">TERMS &amp; PRIVACY</span>
  <span style="left:517px">|</span>
  <span style="left:544px">HELP</span>
  <span style="left:596px">|</span>
  <span style="left:622px">LUMO APP</span>
  <span style="left:719px">|</span>
  <span style="left:745px">VERDA APP</span>
</footer>

</body>
</html>
```